Simply Mara Website Relaunch - Homepage Design

Current Website: www.simplymara.example

We are looking for a re-design of the Simply Mara website homepage, which will be the start of whole website redesign. The purpose of this website redesign is twofold. First, we need to improve the consistency of the visual design and make sure that it is mobile-optimized (mobile-first design). Second, we want to re-create the site with extensive integration of editorial and “product feature” content that increases user engagement with the site and also improves SEO. So this design will be a commerce/blog site, with the blog content seamlessly integrated into the commerce site, not a separate part of the site.

The new website will be built as a headless, progressive web application (PWA) with a Quarvix ecommerce backend. The headless frontend will integrate with a blog platform, to allow for full integration of commerce and editorial content. Designer does not need to complete any programming, but should keep in mind that we are not limited by traditional ecommerce platforms.

Future Business
SimplyMara.example will focus on becoming a marketplace for gifts and customized products that are related to specific events and people in the life of a woman - weddings, maternity, birthdays, graduations, holidays and family relationships (mom, dad, sister, brother). We are going to expand the product offering of Simply Mara into more product types (household items, decorations, knick-knacks), beyond the rhinestone apparel on the site now.

Simply Mara is a curated collection of products. We will select a small collection of the best product ideas, from reliable vendors.

The new Simply Mara website will be chock full of editorial content related to the events in family life. The future of Simply Mara is a hybrid site, commerce and content, wrapped together in a wonderful package. An example of site that integrates editorial content and commerce is https://www.thecozypetalnook.example, although this site is more of a blog with commerce integrated and we want an ecommerce site with blog integrated.

Creative Direction
The visual style of Simply Mara should be driven by the product merchandising and editorial content sections. Although we want a strong brand identity, the branding needs to not conflict or over-power the content of the site.

Colors:
We are open to a completely new color scheme, or to using the current salmon color. The colors should skew slightly female, but not so far that we cannot sell products for men on the site.

Logo:
We like the icon in our current logo, but don’t like the current type style. We are also open to creating a new logo, or changing the treatment of our current logo. This will be a separate project.

Homepage Design Task
The homepage design needs to weave together commerce and content sections. Below is the content that needs to be featured on this page.

Commerce Content
Custom Rhinestone Apparel - Banner highlighting our custom rhinestone apparel. On our existing site, www.simplymara.example, the top 2 sections are both about custom rhinestone apparel, but this should be merged into one message, so it is more efficient.

Everyday - A collection of everyday rhinestone fashions. Our “everyday” products will be tops and activewear that is embellished with rhinestone accents. I can provide more details if needed.

Celebrate! - Section that highlights all the life events that fall into celebrations - birthday, maternity, graduation, anniversary. This section could also include an editorial part that is an article related to a holiday or celebration event.

Spiritwear - Section that highlights our cheer and sports team custom designs.

Deal of the Day - A deal of the day banner that features the best deals from each of our major product categories.

Editorial Content
Featured Lookbook - Lookbook section for one of the main product categories. A lookbook is a collection of items that go together in a collection.

Article Highlight - An article with related content that is featured in the section. For example, in the spiritwear section, there might be an article on how to get a team prepared for competition. These article highlights would link to the full page design.

Lifestyle Feature - A post related to overall lifestyle of the target audience. This could be fashion, home decor or event planning related and will swap out on a regular basis.

Deal of the Week/Day - Rotating product deal feature that will create daily freshness to the site. This section should pull a deal from several of our product categories.

Gift Idea - Review of a cool gift idea for a specific occasion.

Target Market(s)

Females aged 22-50 – products for themselves and gifts for children and friends. Our target audience is middle-to-upper-class, but still wants value for their money.

Please keep in mind that our target audience is not the teenage crowd, and we are not a trend-driven brand.

Number of Pages Required

1 page

Requirements
Must have
• Deliverable on this project is a homepage design only, however, the design will set the direction for the rest of the site. The winning designer may have an opportunity to do work on many more interior pages and landing pages.

The design must be designed so that it can be responsively programmed and will work as a mobile design.
Nice to have
• Good organization of content on the page that can be used as a template for other pages on the site. In particular, the integration of commerce and content elements effectively will be very important.

```html
<!DOCTYPE html>
<html lang="en">
<head>
<meta charset="utf-8">
<title>Simply Mara — Homepage</title>
<link href="https://fonts.googleapis.com/css2?family=Montserrat:ital,wght@0,400;0,500;0,600;1,300;1,400&family=Open+Sans:wght@400;600&display=swap" rel="stylesheet">
<style>
:root{
  --salmon:#f27a7a;
  --salmon-dark:#e86464;
  --blush:#fde8e8;
  --blush-deep:#f9d4d4;
  --ink:#3b3b3b;
  --muted:#8a8a8a;
  --white:#ffffff;
  --line:#ececec;
}
*{box-sizing:border-box;margin:0;padding:0}
html,body{width:1200px;height:3752px;overflow:hidden}
body{font-family:"Open Sans",Arial,sans-serif;color:var(--ink);background:var(--white);font-size:13px;line-height:1.6}
.section-title{font-family:"Montserrat",Arial,sans-serif;font-style:italic;font-weight:400;font-size:26px;letter-spacing:3px;text-transform:uppercase;text-align:center;color:var(--ink)}
.section{position:relative;width:1200px}
.section--blush{background:var(--blush)}
.btn{display:inline-block;background:var(--salmon);color:var(--white);font-size:12px;border-radius:20px;padding:7px 22px;text-decoration:none}
.btn--outline{background:transparent;border:1.5px solid var(--white)}
.link-more{color:var(--salmon);font-size:12px;text-decoration:underline}
.arrow{position:absolute;width:20px;height:20px}
.dots{display:flex;gap:8px;justify-content:center}
.dots span{width:8px;height:8px;border-radius:50%;background:var(--salmon);opacity:.45}
.dots span.on{opacity:1}

/* header */
.site-header{height:68px;display:flex;align-items:center;padding:0 72px;background:var(--white);position:relative;z-index:2}
.brand{display:flex;align-items:center;gap:10px;font-family:"Montserrat",Arial,sans-serif;font-weight:500;font-size:26px;color:var(--ink)}
.brand-mark{width:28px;height:28px;background:var(--salmon)}
.main-nav{display:flex;align-items:center;gap:42px;margin-left:auto;margin-right:100px;font-size:13px}
.main-nav .active{border:1.5px solid var(--salmon);color:var(--salmon);border-radius:20px;padding:3px 26px}

/* hero */
.hero{height:380px;background:linear-gradient(180deg,#5d6a58 0%,#7c8a6c 45%,#3f4c37 75%,#8b4a3c 100%);position:relative}
.hero-photo{position:absolute;inset:0}
.hero-copy{position:absolute;left:148px;top:88px;color:var(--white);width:460px}
.hero-copy h1{font-family:"Montserrat",Arial,sans-serif;font-style:italic;font-weight:400;font-size:30px;letter-spacing:2px;text-transform:uppercase}
.hero-copy p{font-size:13px;margin:10px 0 56px;opacity:.9}

/* everyday */
.everyday{height:512px;padding-top:40px}
.product-row{position:absolute;top:92px;left:176px;display:flex;gap:29px}
.product-card{width:190px;height:372px;background:var(--white);box-shadow:0 2px 14px rgba(0,0,0,.12);text-align:center;padding:8px 8px 0}
.product-photo{height:200px;background:linear-gradient(180deg,#c9b7a4,#6f5a4c)}
.product-card h3{font-size:11px;font-weight:600;margin-top:14px}
.product-card .price{color:var(--salmon);font-size:12px;margin:14px 0 8px}
.product-card p{font-size:10px;color:var(--muted);padding:0 10px;line-height:1.5}

/* celebrate */
.celebrate{height:440px;padding-top:44px}
.occasion-row{position:absolute;top:104px;left:152px;display:flex;gap:108px}
.occasion{width:228px;text-align:center}
.occasion-photo{height:148px}
.occasion h3{font-family:"Montserrat",Arial,sans-serif;font-weight:400;font-size:20px;letter-spacing:1px;margin:22px 0 8px}
.occasion p{font-size:11px;color:var(--muted);line-height:1.5}

/* spiritwear */
.spiritwear{height:388px;padding-top:36px}
.spirit-photos{position:absolute;top:92px;left:152px;width:896px;height:260px;display:flex}
.spirit-photos div{flex:1}

/* deal of the day */
.deals{height:372px;padding-top:40px}
.deal-row{position:absolute;top:92px;left:352px;display:flex;gap:56px}
.deal-card{width:224px;height:192px;background:var(--white);box-shadow:0 2px 14px rgba(0,0,0,.1);display:flex}
.deal-photo{width:100px;background:linear-gradient(180deg,#d9c0b5,#ee9fb0)}
.deal-body{padding:30px 12px;font-size:10px;color:var(--muted);line-height:1.5}
.deal-body h3{font-size:12px;color:var(--ink);font-weight:600;margin-bottom:16px}
.deals .dots{position:absolute;top:320px;left:0;right:0}

/* holidays */
.holidays{height:352px;padding-top:36px}
.holiday-row{position:absolute;top:88px;left:152px;width:896px;height:224px;display:flex}
.holiday-row div{flex:1}

/* articles */
.article{height:428px;padding-top:40px}
.lifestyle{height:432px;padding-top:32px}
.feature-card{position:absolute;left:152px;width:896px;height:296px;background:var(--white);box-shadow:0 2px 16px rgba(0,0,0,.1);display:flex}
.feature-photo{width:320px}
.feature-body{flex:1;padding:50px 36px 30px;position:relative}
.feature-body h2{font-size:16px;font-weight:600;margin-bottom:18px}
.feature-body p{font-size:11px;color:var(--muted);line-height:1.7}
.feature-body .link-more{position:absolute;left:36px;bottom:36px}
.feature-body .date{position:absolute;right:36px;bottom:36px;font-size:11px;color:var(--muted)}

/* gift */
.gift{height:240px;background:linear-gradient(120deg,#e98aa0 0%,#f5b7c4 40%,#e3586e 70%,#f6c4a0 100%);text-align:center;color:var(--white);padding-top:34px}
.gift .section-title{color:var(--white)}
.gift p{width:560px;margin:14px auto 20px;font-size:12px;line-height:1.6}

/* footer */
.site-footer{height:152px;background:var(--salmon);color:var(--white);display:flex;padding:28px 152px 0;gap:60px;font-size:11px}
.site-footer h4{font-size:13px;font-weight:600;margin-bottom:10px}
.foot-welcome{width:300px;line-height:1.6}
.foot-links{display:flex;gap:36px}
.foot-links ul{list-style:none;line-height:1.9}
.foot-news{margin-left:auto;width:300px}
.subscribe{display:flex;margin-top:6px}
.subscribe span{flex:1;height:30px;background:var(--white)}
.subscribe b{background:var(--salmon-dark);padding:6px 20px;font-weight:600}
</style>
</head>
<body>

<header class="site-header">
  <div class="brand"><span class="brand-mark"></span>simply mara</div>
  <nav class="main-nav">
    <span class="active">Home</span><span>Shops</span><span>Custom</span><span>Brands</span><span>Help</span><span>Promotions</span>
    <svg width="18" height="16" viewBox="0 0 18 16"><path d="M1 1h3l2 9h9l2-6H5" fill="none" stroke="#f27a7a" stroke-width="1.6"/><circle cx="7" cy="14" r="1.4" fill="#f27a7a"/><circle cx="14" cy="14" r="1.4" fill="#f27a7a"/></svg>
  </nav>
</header>

<section class="hero">
  <div class="hero-photo" role="img" aria-label="Woman in a rhinestone top standing in a park"></div>
  <div class="hero-copy">
    <h1>Custom Rhinestone Apparel</h1>
    <p>Sparkle made just for you. Design your own rhinestone tee for any team, event or celebration.</p>
    <a class="btn" href="#">Shop Now</a>
  </div>
</section>

<section class="section everyday">
  <h2 class="section-title">Everyday</h2>
  <svg class="arrow" style="left:140px;top:270px" viewBox="0 0 20 20"><path d="M13 3 6 10l7 7" fill="none" stroke="#f27a7a" stroke-width="2"/></svg>
  <div class="product-row">
    <article class="product-card"><div class="product-photo" role="img" aria-label="Woman wearing a black rhinestone tee"></div><h3>Rhinestone Crew Shirt</h3><div class="price">$24.00</div><p>Soft cotton tee finished with hand set sparkle accents.</p></article>
    <article class="product-card"><div class="product-photo" role="img" aria-label="Woman wearing a black rhinestone top"></div><h3>Rhinestone Crew Shirt</h3><div class="price">$24.00</div><p>Soft cotton tee finished with hand set sparkle accents.</p></article>
    <article class="product-card"><div class="product-photo" role="img" aria-label="Woman wearing a white rhinestone tee"></div><h3>Rhinestone Crew Shirt</h3><div class="price">$24.00</div><p>Soft cotton tee finished with hand set sparkle accents.</p></article>
    <article class="product-card"><div class="product-photo" role="img" aria-label="Woman wearing a black rhinestone tank"></div><h3>Rhinestone Crew Shirt</h3><div class="price">$24.00</div><p>Soft cotton tee finished with hand set sparkle accents.</p></article>
  </div>
  <svg class="arrow" style="left:1040px;top:270px" viewBox="0 0 20 20"><path d="M7 3l7 7-7 7" fill="none" stroke="#f27a7a" stroke-width="2"/></svg>
</section>

<section class="section section--blush celebrate">
  <h2 class="section-title">Celebrate!</h2>
  <div class="occasion-row">
    <div class="occasion"><div class="occasion-photo" role="img" aria-label="Pink party balloons" style="background:linear-gradient(135deg,#fbe3e6,#f4a6b6)"></div><h3>BIRTHDAY</h3><p>Lorem ipsum gifts for every age, wrapped in sparkle and made to mark the big day.</p></div>
    <div class="occasion"><div class="occasion-photo" role="img" aria-label="Expecting mother silhouette" style="background:linear-gradient(135deg,#e9d6d6,#6b5656)"></div><h3>MATERNITY</h3><p>Sweet keepsakes and comfy tees for moms to be and the friends who love them.</p></div>
    <div class="occasion"><div class="occasion-photo" role="img" aria-label="Graduates in caps and gowns" style="background:linear-gradient(135deg,#f7c6cf,#d26a80)"></div><h3>GRADUATION</h3><p>Celebrate the grad with custom shirts, gifts and décor in school colors.</p></div>
  </div>
</section>

<section class="section spiritwear">
  <h2 class="section-title">Spiritwear</h2>
  <div class="spirit-photos">
    <div role="img" aria-label="Volleyball team playing in a gym" style="background:linear-gradient(135deg,#b8a79a,#6d5d52)"></div>
    <div role="img" aria-label="Cheerleaders performing in front of a crowd" style="background:linear-gradient(135deg,#7a6a7c,#c3aa9a)"></div>
  </div>
</section>

<section class="section section--blush deals">
  <h2 class="section-title">Deal of the Day</h2>
  <svg class="arrow" style="left:146px;top:198px" viewBox="0 0 20 20"><path d="M13 3 6 10l7 7" fill="none" stroke="#f27a7a" stroke-width="2"/></svg>
  <div class="deal-row">
    <article class="deal-card"><div class="deal-photo" role="img" aria-label="Woman in a pink hoodie"></div><div class="deal-body"><h3>Initial Hoodie Sweats</h3>Cozy fleece hoodie with a sparkling initial, today only.</div></article>
    <article class="deal-card"><div class="deal-photo" role="img" aria-label="Woman in a pink hoodie"></div><div class="deal-body"><h3>Initial Hoodie Sweats</h3>Cozy fleece hoodie with a sparkling initial, today only.</div></article>
  </div>
  <svg class="arrow" style="left:1040px;top:198px" viewBox="0 0 20 20"><path d="M7 3l7 7-7 7" fill="none" stroke="#f27a7a" stroke-width="2"/></svg>
  <div class="dots"><span class="on"></span><span></span><span></span></div>
</section>

<section class="section holidays">
  <h2 class="section-title">Holidays</h2>
  <div class="holiday-row">
    <div role="img" aria-label="Woman in a patriotic holiday tee" style="background:linear-gradient(180deg,#c8b6a8,#7a8aa8)"></div>
    <div role="img" aria-label="Woman in a black holiday tee" style="background:linear-gradient(180deg,#d9cfc4,#3a3a3a)"></div>
    <div role="img" aria-label="Woman in a white festive tee" style="background:linear-gradient(180deg,#e8dccf,#bfa890)"></div>
    <div role="img" aria-label="Woman in a pink holiday top" style="background:linear-gradient(180deg,#efd0d2,#e9a5b0)"></div>
    <div role="img" aria-label="Woman in a black sparkle tee" style="background:linear-gradient(180deg,#d6c0b0,#2f2f2f)"></div>
  </div>
</section>

<section class="section section--blush article">
  <h2 class="section-title">Article Highlight</h2>
  <article class="feature-card" style="top:92px">
    <div class="feature-photo" role="img" aria-label="Runners racing on a track" style="background:linear-gradient(135deg,#c96a4e,#6b5a7a)"></div>
    <div class="feature-body">
      <h2>How to Get a Team Prepared for Competition</h2>
      <p>Great teams start long before the first whistle. From matching warm ups to a shared pre game routine, small details help athletes feel ready, confident and united. Here are our favorite ways to build spirit, plan practice schedules and keep the whole squad focused through the season, plus a few custom pieces that help every member shine.</p>
      <a class="link-more" href="#">Read more</a><span class="date">June 12, 2019</span>
    </div>
  </article>
</section>

<section class="section lifestyle">
  <h2 class="section-title">Lifestyle Feature</h2>
  <article class="feature-card" style="top:92px">
    <div class="feature-body">
      <h2>How to Plan the Perfect Event</h2>
      <p>Whether it is a backyard birthday or a shower for a close friend, a little planning makes the day feel effortless. Start with a simple theme, pick a color palette, and build a guest list early. We share our checklist for invitations, décor and favors, plus easy ideas to personalize every table.</p>
      <a class="link-more" href="#">Read more</a><span class="date">June 12, 2019</span>
    </div>
    <div class="feature-photo" role="img" aria-label="Open planner notebook on a table" style="background:linear-gradient(135deg,#eeeeee,#a9a9a9);width:296px"></div>
  </article>
</section>

<section class="section gift" role="img" aria-label="Pink gift box with ribbon">
  <h2 class="section-title">Gift Idea</h2>
  <p>A sparkling keepsake box filled with a custom tee, a matching tote and a handwritten note makes the perfect gift for any friend celebrating a milestone this season.</p>
  <a class="btn btn--outline" href="#">Read More</a>
</section>

<footer class="site-footer">
  <div class="foot-welcome"><h4>Welcome to SimplyMara.example</h4>Curated gifts and custom rhinestone apparel for the moments that matter most in family life, chosen with care and made to last.</div>
  <div><h4>Quick Links</h4>
    <div class="foot-links">
      <ul><li>Birthday</li><li>Maternity</li><li>Graduation</li></ul>
      <ul><li>FAQ</li><li>Shipping</li><li>Contact</li></ul>
    </div>
  </div>
  <div class="foot-news"><h4>Subscribe to our newsletter</h4><div class="subscribe"><span></span><b>Send</b></div></div>
</footer>

</body>
</html>
```